Disability Service Provider Expo Banner that will stand out amongst the competition

We would like to have a two banners designed to be able to display at expos that outline the services that we provide as a company. We are a disability service provider who aims to provider services to increase the independence of those living with a disability. We would like the banners to follow consistent themes/designs from other marketing material that we have (see brief for designs). One of the banners will be for the allied health services we provide (exercise physiology and occupational therapy) and the other banner will be promoting the our support worker, programs, and short-term accommodation. Our main colour schemes for therapy are black, yellow, and white. For our other services we utilise yellow, blue, and magenta as part of our colour pallet. Please utilise the information from the flyers, colours, and logos all located in the design brief. The style of banner can be seen in the images upload in the brief.

Target Market(s)

Parents and carers of those who livce with a disability, and seeking their business over our competitors

Industry/Entity Type

Disability Service and Health Provider

Colors

Designer to choose colors to be used in the design.

Requirements
Must have
• Eye catching, limited text
Nice to have
• Split services across a few banners
Should not have
• Lots of words

```html
<!DOCTYPE html>
<html lang="en">
<head>
<meta charset="utf-8">
<title>Brightvale Pull Up Banners</title>
<link rel="stylesheet" href="https://fonts.googleapis.com/css2?family=Montserrat:ital,wght@0,400;0,500;0,700;0,800;1,800&display=swap">
<style>
  :root {
    --page: #e6e6e8;
    --white: #ffffff;
    --ink: #111111;
    --blue: #3a93d3;
    --blue-deep: #2f86c9;
    --yellow: #fbd83a;
    --pill-grey: #d4d4d6;
    --dot: #9a9a9a;
  }
  * { box-sizing: border-box; margin: 0; padding: 0; }
  html, body { width: 1187px; height: 1200px; overflow: hidden; }
  body {
    background: var(--page);
    font-family: "Montserrat", Arial, sans-serif;
    color: var(--ink);
    position: relative;
  }
  .banner {
    position: absolute;
    top: 116px;
    width: 409px;
    height: 932px;
    background: var(--white);
    overflow: hidden;
    box-shadow: 0 10px 24px rgba(0,0,0,0.28);
  }
  .banner--therapy { left: 165px; }
  .banner--services { left: 616px; }

  .corner { position: absolute; border-radius: 50%; }
  .corner--blue { width: 124px; height: 124px; background: var(--blue); left: 308px; top: -22px; }
  .corner--yellow { width: 80px; height: 80px; background: var(--yellow); left: 279px; top: -30px; }

  .brand { position: absolute; left: 0; right: 0; text-align: center; }
  .brand__dot {
    display: block; width: 46px; height: 46px; border-radius: 50%;
    background: var(--yellow); margin: 0 auto 14px;
  }
  .brand__name { font-weight: 800; font-size: 38px; letter-spacing: 0.5px; line-height: 1; }
  .banner--therapy .brand { top: 66px; }
  .banner--services .brand { top: 56px; }

  .headline {
    position: absolute; top: 204px; left: 0; right: 0; text-align: center;
    color: var(--blue); font-weight: 800; font-size: 43px; line-height: 47px; letter-spacing: -0.5px;
  }
  .lede {
    position: absolute; top: 305px; left: 0; right: 0; text-align: center;
    font-size: 16px; line-height: 22.5px; font-weight: 500;
  }
  .lede strong { font-weight: 800; }

  .hero-photo {
    position: absolute; left: 0; top: 385px; width: 409px; height: 547px;
    background: linear-gradient(180deg, #ffffff 0%, #dfe8ef 10%, #8fb4cc 30%, #5d7280 50%, #3b3f44 66%, #141414 82%, #0a0a0a 100%);
  }

  .pills { position: absolute; top: 718px; left: 27px; width: 361px; height: 32px; }
  .pill {
    position: absolute; top: 0; height: 32px; border-radius: 5px;
    display: flex; align-items: center; justify-content: center;
    font-weight: 800; font-style: italic; font-size: 15px;
    background: var(--pill-grey); box-shadow: 0 3px 6px rgba(0,0,0,0.45);
  }
  .pill--fit { left: 0; width: 107px; }
  .pill--healthy { left: 113px; width: 132px; background: var(--yellow); }
  .pill--fun { left: 251px; width: 110px; }

  .footer { position: absolute; left: 0; bottom: 0; width: 409px; height: 145px; }
  .footer svg { position: absolute; inset: 0; }
  .footer__text { position: absolute; left: 0; right: 0; top: 54px; text-align: center; color: var(--white); }
  .footer__call {
    display: flex; align-items: center; justify-content: center; gap: 8px;
    font-size: 26px; font-weight: 500; line-height: 30px;
  }
  .footer__call strong { font-weight: 800; }
  .footer__web { font-size: 22px; line-height: 30px; font-weight: 500; }
  .footer__web strong { font-weight: 800; }
  .phone-icon { width: 26px; height: 26px; }

  .photo-circle {
    position: absolute; border-radius: 50%; border: 2px solid var(--blue);
  }
  .photo-circle--friends { left: 75px; top: 184px; width: 180px; height: 180px; background: linear-gradient(135deg, #f3ead8, #c9a47f 55%, #6d5646); z-index: 3; }
  .photo-circle--team { left: 194px; top: 254px; width: 186px; height: 186px; background: linear-gradient(160deg, #4e7a3c, #8fb3d2 55%, #5f88b5); z-index: 1; border: 0; }
  .photo-circle--team { border: 2px solid var(--blue); }
  .photo-circle--mates { left: 32px; top: 337px; width: 174px; height: 174px; background: linear-gradient(160deg, #8c9a6c, #55504a 55%, #2e2f33); z-index: 2; border: 0; }
  .photo-circle--selfie { left: 192px; top: 420px; width: 124px; height: 124px; background: linear-gradient(150deg, #b9c6d6, #c98f6e 50%, #3c3d4a); z-index: 4; }
  .photo-circle--crafts { left: 102px; top: 473px; width: 114px; height: 114px; background: linear-gradient(160deg, #e4ecf3, #d9c2b0 55%, #9fb0c4); z-index: 5; }

  .services-title {
    position: absolute; top: 620px; left: 30px; width: 349px; height: 30px;
  }
  .services-title__rule {
    position: absolute; top: 14px; left: 0; width: 100%; height: 2px;
    background: linear-gradient(90deg, transparent, var(--yellow) 30%, var(--yellow) 70%, transparent);
  }
  .services-title__label {
    position: absolute; left: 99px; top: 0; width: 152px; height: 30px; border-radius: 15px;
    background: var(--yellow); font-weight: 800; font-size: 19px; line-height: 30px; text-align: center;
  }

  .service-grid { position: absolute; top: 666px; left: 22px; width: 370px; height: 110px; }
  .service {
    position: absolute; width: 124px; text-align: center;
    font-size: 15.5px; line-height: 19.5px; font-weight: 500;
  }
  .service--c1 { left: -8px; }
  .service--c2 { left: 126px; width: 132px; }
  .service--c3 { left: 256px; }
  .service--r1 { top: 0; }
  .service--r2 { top: 57px; }
  .service--single { top: 67px; }
  .service-grid .rule-v { position: absolute; top: 0; height: 98px; border-left: 1.5px dotted var(--dot); }
  .rule-v--a { left: 117px; }
  .rule-v--b { left: 268px; }
  .service-grid .rule-h { position: absolute; top: 48px; height: 0; border-top: 1.5px dotted var(--dot); }
  .rule-h--a { left: 0; width: 108px; }
  .rule-h--b { left: 126px; width: 134px; }
  .rule-h--c { left: 276px; width: 92px; }
</style>
</head>
<body>

<section class="banner banner--therapy">
  <div class="hero-photo" role="img" aria-label="Exercise physiologist guiding a woman with a prosthetic leg through floor exercises in a gym"></div>
  <div class="corner corner--blue"></div>
  <div class="corner corner--yellow"></div>

  <div class="brand">
    <span class="brand__dot"></span>
    <div class="brand__name">BRIGHTVALE</div>
  </div>

  <h1 class="headline">EXERCISE<br>PHYSIOLOGY</h1>
  <p class="lede">Improve your <strong>health, quality of life,</strong><br><strong>&amp; independence</strong> with the help of<br>our Excersise Physiologist!</p>

  <div class="pills">
    <div class="pill pill--fit">GET FIT</div>
    <div class="pill pill--healthy">BE HEALTHY</div>
    <div class="pill pill--fun">HAVE FUN</div>
  </div>

  <div class="footer">
    <svg width="409" height="145" viewBox="0 0 409 145">
      <path fill="var(--blue)" d="M0,50 Q18,55 28,66 C34,12 88,0 118,0 C152,0 178,18 194,38 C214,22 248,20 262,34 C276,10 300,6 320,6 C352,6 372,30 380,62 Q396,60 409,52 L409,145 L0,145 Z"/>
    </svg>
    <div class="footer__text">
      <div class="footer__call">
        <svg class="phone-icon" viewBox="0 0 26 26"><circle cx="13" cy="13" r="13" fill="#111"/><path fill="#fff" d="M9.2 6.5l2 2.6c.3.4.3.9 0 1.3l-1 1c.7 1.6 2 2.9 3.6 3.7l1-1c.4-.3.9-.3 1.3 0l2.5 2c.4.3.4.9.1 1.3l-1 1.1c-.6.6-1.5.8-2.3.5-4-1.4-7-4.5-8.4-8.4-.3-.8-.1-1.7.5-2.3l1-1c.3-.3.9-.3 1.2.1z"/></svg>
        <span>Call <strong>1800 000 123</strong></span>
      </div>
      <div class="footer__web">www.<strong>brightvale.com</strong>.au</div>
    </div>
  </div>
</section>

<section class="banner banner--services">
  <div class="corner corner--blue"></div>
  <div class="corner corner--yellow"></div>

  <div class="brand">
    <span class="brand__dot"></span>
    <div class="brand__name">BRIGHTVALE</div>
  </div>

  <div class="photo-circle photo-circle--friends" role="img" aria-label="Two smiling young women embracing outdoors"></div>
  <div class="photo-circle photo-circle--team" role="img" aria-label="Group of young people in blue shirts joining hands in a team huddle"></div>
  <div class="photo-circle photo-circle--mates" role="img" aria-label="Three men in wheelchairs together in a park"></div>
  <div class="photo-circle photo-circle--selfie" role="img" aria-label="Friends laughing together in a group selfie"></div>
  <div class="photo-circle photo-circle--crafts" role="img" aria-label="Two young women doing a craft activity at a table"></div>

  <div class="services-title">
    <div class="services-title__rule"></div>
    <div class="services-title__label">Our Services</div>
  </div>

  <div class="service-grid">
    <span class="rule-v rule-v--a"></span>
    <span class="rule-v rule-v--b"></span>
    <span class="rule-h rule-h--a"></span>
    <span class="rule-h rule-h--b"></span>
    <span class="rule-h rule-h--c"></span>
    <div class="service service--c1 service--r1">Support<br>Workers</div>
    <div class="service service--c2 service--r1">Day Programs<br>&amp; Workshops</div>
    <div class="service service--c3" style="top:-2px">Group<br>Activities</div>
    <div class="service service--c1 service--r2">Living Skills<br>Programs</div>
    <div class="service service--c2 service--r2">STA/Supported<br>Holiday</div>
    <div class="service service--c3 service--r2">Therapies</div>
  </div>

  <div class="footer">
    <svg width="409" height="145" viewBox="0 0 409 145">
      <path fill="var(--blue)" d="M0,50 Q18,55 28,66 C34,12 88,0 118,0 C152,0 178,18 194,38 C214,22 248,20 262,34 C276,10 300,6 320,6 C352,6 372,30 380,62 Q396,60 409,52 L409,145 L0,145 Z"/>
    </svg>
    <div class="footer__text">
      <div class="footer__call">
        <svg class="phone-icon" viewBox="0 0 26 26"><circle cx="13" cy="13" r="13" fill="#111"/><path fill="#fff" d="M9.2 6.5l2 2.6c.3.4.3.9 0 1.3l-1 1c.7 1.6 2 2.9 3.6 3.7l1-1c.4-.3.9-.3 1.3 0l2.5 2c.4.3.4.9.1 1.3l-1 1.1c-.6.6-1.5.8-2.3.5-4-1.4-7-4.5-8.4-8.4-.3-.8-.1-1.7.5-2.3l1-1c.3-.3.9-.3 1.2.1z"/></svg>
        <span>Call <strong>1800 000 123</strong></span>
      </div>
      <div class="footer__web">www.<strong>brightvale.com</strong>.au</div>
    </div>
  </div>
</section>

</body>
</html>
```